" Atuamos como laboratório de análises clínicas, oferecendo exames laboratoriais para diagnóstico e prevenção de doenças. Nosso atendimento é feito tanto para pacientes particulares quanto por convênios, com coleta realizada em nossa unidade por profissionais qualificados. Os resultados são disponibilizados de forma rápida, podendo ser acessados online ou retirados presencialmente. Trabalhamos com foco em qualidade, confiabilidade e atendimento humanizado. "

```html
<!DOCTYPE html>
<html lang="pt-BR">
<head>
<meta charset="UTF-8">
<title>Assinatura de e-mail – Vitalab</title>
<link href="https://fonts.googleapis.com/css2?family=Montserrat:wght@400;500;700&display=swap" rel="stylesheet">
<style>
  :root {
    --page: #ffffff;
    --ink: #2b2b2b;
    --ink-soft: #555555;
    --green-deep: #1f6b45;
    --green: #2f9e63;
    --green-pale: #dcefe3;
  }
  html, body {
    margin: 0;
    width: 1200px;
    height: 1200px;
    overflow: hidden;
    background: var(--page);
    font-family: "Montserrat", Arial, sans-serif;
    color: var(--ink);
  }
  .signature {
    position: absolute;
    left: 120px;
    top: 430px;
    width: 960px;
    height: 340px;
    display: flex;
    align-items: center;
    justify-content: space-between;
  }
  .contact {
    position: relative;
    padding-left: 40px;
    border-left: 6px solid var(--green);
    line-height: 1.35;
  }
  .contact__name {
    margin: 0 0 10px;
    font-size: 30px;
    font-weight: 700;
    color: var(--ink);
  }
  .contact__line {
    margin: 0;
    font-size: 19px;
    font-weight: 400;
    color: var(--ink-soft);
  }
  .contact__group { margin-top: 22px; }
  .contact__address { margin-top: 22px; }
  .contact__address .contact__line { font-size: 16px; }

  .brand {
    position: relative;
    width: 420px;
    height: 300px;
  }
  .brand__bands {
    position: absolute;
    inset: 0;
  }
  .brand__name {
    position: absolute;
    left: 70px;
    top: 150px;
    display: flex;
    align-items: center;
    gap: 18px;
    font-size: 58px;
    font-weight: 500;
    color: var(--green-deep);
  }
  .brand__dot {
    width: 34px;
    height: 34px;
    border-radius: 50%;
    background: var(--green);
  }
</style>
</head>
<body>
  <section class="signature">
    <div class="contact">
      <h1 class="contact__name">Dra. Helena Vasconi</h1>
      <p class="contact__line">CRFMG 20.318</p>
      <p class="contact__line">Direção</p>
      <div class="contact__group">
        <p class="contact__line">35 3200.4180</p>
        <p class="contact__line">vitalabcentro@email.com</p>
        <p class="contact__line">vitalab.com.br</p>
      </div>
      <div class="contact__address">
        <p class="contact__line">Rua das Acácias, 210/214</p>
        <p class="contact__line">Centro - Serra Alta - MG - Cep 37400-000</p>
      </div>
    </div>

    <div class="brand">
      <svg class="brand__bands" viewBox="0 0 420 300" aria-hidden="true">
        <polygon points="40,300 90,20 150,20 100,300" fill="var(--green-pale)"/>
        <polygon points="300,300 340,120 400,120 360,300" fill="var(--green-pale)"/>
      </svg>
      <div class="brand__name">
        <span class="brand__dot"></span>
        <span>Vitalab</span>
      </div>
    </div>
  </section>
</body>
</html>
```